Tarvel Ridge LLC

Need Professional Business cards for New Investment Fund

Target Market(s)

High Quality investors

Industry/Entity Type

Financial

Contact Information for Business Card

Phone Number +1 555 284 6193
Name Pavel Orlinsky
Title Fund Manager
email po@FundTarvel.example
Website www.FundTarvel.example

Colors

Designer to choose colors to be used in the design.

Requirements
Must have
• Must have our Logo and all of the above. Must be made so lettering and loge can be raised

```html
<!DOCTYPE html>
<html lang="en">
<head>
<meta charset="utf-8">
<title>Tarvel Ridge LLC – Business Card</title>
<link rel="stylesheet" href="https://fonts.googleapis.com/css2?family=Arimo:wght@400;700&display=swap">
<style>
  :root {
    --brand-green: #5bbb46;
    --ink-dark: #3d4a3f;
    --ink-body: #555b56;
    --paper: #ffffff;
    --backdrop: #e9e7e3;
  }
  * { margin: 0; padding: 0; box-sizing: border-box; }
  html, body { width: 1200px; height: 800px; overflow: hidden; }
  body {
    background: var(--backdrop);
    font-family: "Arimo", Arial, sans-serif;
    position: relative;
  }
  .card {
    position: absolute;
    top: 250px;
    width: 520px;
    height: 300px;
    overflow: hidden;
    box-shadow: 0 6px 18px rgba(0,0,0,0.18);
  }
  .card--front { left: 50px; background: var(--paper); }
  .card--back { left: 630px; background: var(--brand-green); }

  .card__swoosh { position: absolute; left: 0; top: 0; width: 520px; height: 300px; }

  .brand-mark {
    position: absolute;
    display: flex;
    align-items: center;
    gap: 10px;
    font-weight: 700;
    white-space: nowrap;
  }
  .brand-mark__square { display: block; }
  .card--front .brand-mark { left: 38px; top: 112px; color: var(--ink-dark); font-size: 22px; }
  .card--front .brand-mark__square { width: 16px; height: 16px; background: var(--brand-green); }
  .card--back .brand-mark { left: 50%; top: 50%; transform: translate(-50%, -50%); color: var(--paper); font-size: 34px; }

  .contact {
    position: absolute;
    left: 250px;
    top: 42px;
  }
  .contact__name { font-size: 19px; font-weight: 700; color: var(--ink-dark); }
  .contact__title { font-size: 13px; color: var(--ink-body); margin-top: 2px; }
  .contact__list { list-style: none; margin-top: 14px; }
  .contact__item {
    display: flex;
    align-items: center;
    gap: 10px;
    font-size: 14px;
    color: var(--ink-body);
    margin-bottom: 7px;
    white-space: nowrap;
  }
  .contact__icon { width: 14px; height: 14px; flex: none; }
</style>
</head>
<body>

<section class="card card--front">
  <svg class="card__swoosh" viewBox="0 0 520 300" aria-hidden="true">
    <path d="M0 274 Q300 266 520 192 L520 300 L0 300 Z" fill="var(--brand-green)"/>
    <path d="M0 262 Q300 254 520 178" fill="none" stroke="var(--ink-dark)" stroke-width="4"/>
  </svg>

  <div class="brand-mark">
    <span class="brand-mark__square"></span>
    <span class="brand-mark__name">Tarvel Ridge</span>
  </div>

  <div class="contact">
    <p class="contact__name">Pavel Orlinsky</p>
    <p class="contact__title">Fund Manager</p>
    <ul class="contact__list">
      <li class="contact__item">
        <svg class="contact__icon" viewBox="0 0 16 16" aria-hidden="true"><path d="M3.5 1.5l2.5 0 1 3.5-1.6 1.2a8 8 0 0 0 4.4 4.4L11 9l3.5 1v2.5c0 1-1 2-2 2A11.5 11.5 0 0 1 1.5 3.5c0-1 1-2 2-2z" fill="var(--brand-green)"/></svg>
        <span>+1 555 284 6193</span>
      </li>
      <li class="contact__item">
        <svg class="contact__icon" viewBox="0 0 16 16" aria-hidden="true"><rect x="1" y="3" width="14" height="10" fill="var(--brand-green)"/><path d="M1 3.5l7 5 7-5" fill="none" stroke="#fff" stroke-width="1.3"/></svg>
        <span>po@FundTarvel.example</span>
      </li>
      <li class="contact__item">
        <svg class="contact__icon" viewBox="0 0 16 16" aria-hidden="true"><circle cx="8" cy="8" r="7" fill="var(--brand-green)"/><path d="M1 8h14M8 1c-3 3.5-3 10.5 0 14M8 1c3 3.5 3 10.5 0 14" fill="none" stroke="#fff" stroke-width="1"/></svg>
        <span>www.FundTarvel.example</span>
      </li>
    </ul>
  </div>
</section>

<section class="card card--back">
  <div class="brand-mark">
    <span class="brand-mark__name">Tarvel Ridge</span>
  </div>
</section>

</body>
</html>
```